Brookfarrow Osteopathy and dry needling business card

Business card for Brookfarrow Osteopathy and Dry Needling.

Industry/Entity Type

Health

Contact Information for Business Card

I do not have a phone number yet. I also do not have an email address yet. The physical address is: 48 Lower Crane Street Brookfarrow The website is: www.brookfarrowosteosteopathy.example My details are: Dr Martin Pellowe, Osteopath (B.Clin.Sci (Ost) M.Ost BSC ECON (Hons)

Colors
0094D4
00A9DD
6FCCEA
C7EBF8
E9F6FB

Requirements
Must have
• logo on the back
Nice to have
• Maybe a space for me to write an appointment time and date on the card.

```html
<!DOCTYPE html>
<html lang="en">
<head>
<meta charset="utf-8">
<title>Brookfarrow Osteopathy and Dry Needling – Business Card</title>
<link href="https://fonts.googleapis.com/css2?family=Arimo:wght@400;700&display=swap" rel="stylesheet">
<style>
  :root {
    --blue: #0094d4;
    --blue-bright: #00a9dd;
    --blue-deep: #034a73;
    --blue-mid: #0a7fbf;
    --sky: #6fccea;
    --ice: #c7ebf8;
    --mist: #e9f6fb;
    --orange: #f08c1e;
    --ink: #4a4a4a;
    --paper: #ffffff;
    --stage: #eef1f3;
  }
  * { box-sizing: border-box; margin: 0; padding: 0; }
  html, body { width: 1200px; height: 900px; overflow: hidden; }
  body {
    background: var(--stage);
    font-family: "Arimo", Arial, sans-serif;
    display: flex;
    flex-direction: column;
    align-items: center;
    justify-content: center;
    gap: 50px;
  }
  .card {
    position: relative;
    width: 620px;
    height: 354px;
    border-radius: 8px 40px 8px 40px;
    box-shadow: 0 10px 26px rgba(0,0,0,.18);
    overflow: hidden;
  }

  /* Back */
  .card-back {
    background: linear-gradient(200deg, var(--blue-deep) 0%, var(--blue-mid) 100%);
    border-radius: 40px 8px 40px 8px;
  }
  .back-url {
    position: absolute;
    top: 34px;
    right: 36px;
    color: var(--paper);
    font-size: 13px;
    font-weight: 700;
    letter-spacing: 4px;
  }
  .back-url .url-name { color: var(--orange); }
  .back-brand {
    position: absolute;
    left: 60px;
    top: 120px;
    display: flex;
    align-items: center;
    gap: 18px;
  }
  .back-brand-mark {
    width: 150px; height: 150px;
    border-radius: 50%;
    border: 3px solid var(--blue-deep);
  }
  .back-brand-name {
    color: var(--blue-deep);
    font-size: 22px;
    font-weight: 700;
    line-height: 1.25;
    width: 230px;
  }

  /* Front */
  .card-front { background: var(--paper); }
  .front-details {
    position: absolute;
    left: 40px;
    top: 34px;
    width: 380px;
  }
  .person-name {
    color: var(--blue);
    font-size: 22px;
    font-weight: 700;
  }
  .person-title {
    color: var(--orange);
    font-size: 12.5px;
    margin-top: 4px;
  }
  .address {
    color: var(--ink);
    font-size: 13px;
    line-height: 1.35;
    margin-top: 16px;
  }
  .contact-list {
    list-style: none;
    margin-top: 14px;
    color: var(--ink);
    font-size: 13px;
  }
  .contact-list li {
    display: flex;
    align-items: center;
    gap: 8px;
    margin-bottom: 6px;
  }
  .contact-list svg { width: 14px; height: 14px; flex: none; }
  .appointment {
    position: absolute;
    left: 40px;
    bottom: 30px;
    width: 420px;
  }
  .appointment-heading {
    color: var(--blue);
    font-size: 17px;
    font-weight: 700;
    margin-bottom: 14px;
  }
  .appointment-field {
    display: flex;
    align-items: flex-end;
    gap: 8px;
    color: var(--orange);
    font-size: 15px;
    margin-top: 12px;
  }
  .appointment-line {
    flex: 1;
    border-bottom: 2px dotted #777;
    height: 1px;
    margin-bottom: 3px;
  }
  .front-brand {
    position: absolute;
    right: 36px;
    top: 70px;
    width: 170px;
    display: flex;
    flex-direction: column;
    align-items: center;
    gap: 12px;
    text-align: center;
  }
  .front-brand-mark {
    width: 90px; height: 90px;
    border-radius: 50%;
    border: 3px solid var(--blue);
  }
  .front-brand-name {
    color: var(--blue);
    font-size: 15px;
    font-weight: 700;
    line-height: 1.3;
  }
</style>
</head>
<body>

  <section class="card card-back" aria-label="Card back">
    <p class="back-url">www.<span class="url-name">brookfarrowosteosteopathy</span>.example</p>
    <div class="back-brand">
      <div class="back-brand-mark"></div>
      <p class="back-brand-name">Brookfarrow Osteopathy and Dry Needling</p>
    </div>
  </section>

  <section class="card card-front" aria-label="Card front">
    <div class="front-details">
      <h1 class="person-name">Dr Martin Pellowe</h1>
      <p class="person-title">Osteopath (B.Clin.Sci (Ost) M.Ost BSC ECON (Hons)</p>
      <p class="address">48 Lower Crane Street<br>Brookfarrow</p>
      <ul class="contact-list">
        <li>
          <svg viewBox="0 0 16 16" aria-hidden="true"><path d="M3 1.5l2.5 0 1.2 3.2-1.6 1.1a8 8 0 0 0 5.1 5.1l1.1-1.6 3.2 1.2 0 2.5c0 .8-.7 1.5-1.5 1.5A12.5 12.5 0 0 1 1.5 3c0-.8.7-1.5 1.5-1.5z" fill="var(--orange)"/></svg>
          300-200-dummy
        </li>
        <li>
          <svg viewBox="0 0 16 16" aria-hidden="true"><rect x="1" y="3" width="14" height="10" rx="1" fill="var(--orange)"/><path d="M1.5 3.5L8 9l6.5-5.5" stroke="#fff" stroke-width="1.4" fill="none"/></svg>
          info@brookfarrowosteosteopathy.example
        </li>
        <li>
          <svg viewBox="0 0 16 16" aria-hidden="true"><g fill="none" stroke="var(--orange)" stroke-width="1.3"><circle cx="8" cy="8" r="6.5"/><ellipse cx="8" cy="8" rx="3" ry="6.5"/><path d="M1.5 8h13M2.5 4.8h11M2.5 11.2h11"/></g></svg>
          www.brookfarrowosteosteopathy.example
        </li>
      </ul>
    </div>

    <div class="appointment">
      <h2 class="appointment-heading">Your Appointment</h2>
      <div class="appointment-field"><span>Date:</span><span class="appointment-line"></span></div>
      <div class="appointment-field"><span>Time:</span><span class="appointment-line"></span></div>
    </div>

    <div class="front-brand">
      <div class="front-brand-mark"></div>
      <p class="front-brand-name">Brookfarrow Osteopathy and Dry Needling</p>
    </div>
  </section>

</body>
</html>
```